Business Card Design Project

business cards to match the logo design reference 1970674
specific details to be provided asap - message to follow
hello - thank you for the logo design (reference 1970674) which we are very happy with. In terms of business cards you presented a couple of options ie blue front/white back and then the reverse. Can we start with the white front version but change the text details to black font?
Actual details are as follows;
Dorian Whitcombe
Managing Director
e dorianwhitcombe@velantra.com.au
t +61 2 7315 2946
m +61 422 517 639
Suite 307, Level 3, 82 Penhallow St
Sydney, NSW 2000, Australia
www.velantra.com.au

```html
<!DOCTYPE html>
<html lang="en">
<head>
<meta charset="utf-8">
<title>Velantra Business Cards</title>
<link href="https://fonts.googleapis.com/css2?family=Arimo:wght@400;700&family=Open+Sans:wght@600&display=swap" rel="stylesheet">
<style>
  :root {
    --backdrop: #2b2b2b;
    --card: #ffffff;
    --brand-blue: #1a7cc4;
    --brand-sky: #2ba4e0;
    --brand-grey: #636363;
    --ink: #111111;
    --ink-soft: #333333;
  }
  * { margin: 0; padding: 0; box-sizing: border-box; }
  html, body { width: 1200px; height: 1000px; overflow: hidden; }
  body {
    background: var(--backdrop);
    position: relative;
    font-family: "Arimo", Arial, sans-serif;
  }
  .card {
    position: absolute;
    left: 328px;
    width: 592px;
    height: 321px;
    background: var(--card);
    border-radius: 20px;
    overflow: hidden;
  }
  .card--front { top: 171px; }
  .card--back { top: 508px; }

  .brand-mark {
    position: absolute;
    border-radius: 50%;
    background: var(--brand-sky);
  }
  .brand-name {
    position: absolute;
    font-family: "Open Sans", Arial, sans-serif;
    font-weight: 600;
    color: var(--brand-grey);
    white-space: nowrap;
    line-height: 1;
  }
  .card--front .brand-mark { left: 92px; top: 112px; width: 72px; height: 72px; }
  .card--front .brand-name { left: 220px; top: 128px; font-size: 70px; letter-spacing: 1px; }

  .card--back .brand-mark { left: 44px; top: 38px; width: 44px; height: 44px; }
  .card--back .brand-name { left: 106px; top: 60px; font-size: 36px; }
  .website {
    position: absolute;
    left: 107px; top: 102px;
    font-size: 8px; letter-spacing: 2px;
    color: var(--ink-soft);
    text-transform: uppercase;
  }
  .pointer { position: absolute; left: 0; top: 152px; }
  .person-name {
    position: absolute; left: 44px; top: 150px;
    font-size: 19px; font-weight: 700; color: var(--ink);
  }
  .person-role {
    position: absolute; left: 45px; top: 172px;
    font-size: 10px; color: var(--brand-blue);
  }
  .office {
    position: absolute; left: 69px; top: 198px;
    font-size: 11px; line-height: 14px; color: var(--ink-soft);
  }
  .office strong { color: var(--ink); }
  .divider {
    position: absolute; left: 28px; right: 30px; top: 258px;
    height: 2px; background: var(--brand-blue);
  }
  .contact {
    position: absolute; top: 272px;
    font-size: 14px; line-height: 18px; color: var(--ink-soft);
    white-space: nowrap;
  }
  .contact dt { font-size: 13px; font-weight: 700; color: var(--brand-blue); }
  .contact--email { left: 27px; }
  .contact--email dd { font-size: 13px; }
  .contact--phone { left: 250px; }
  .contact--mobile { left: 454px; }
</style>
</head>
<body>
  <section class="card card--front">
    <span class="brand-mark"></span>
    <span class="brand-name">Velantra</span>
  </section>

  <section class="card card--back">
    <span class="brand-mark"></span>
    <span class="brand-name">Velantra</span>
    <span class="website">www.velantra.com.au</span>

    <svg class="pointer" width="20" height="24" viewBox="0 0 20 24" aria-hidden="true">
      <polygon points="0,0 20,12 0,24" fill="#1a7cc4"/>
    </svg>
    <h1 class="person-name">Dorian Whitcombe</h1>
    <p class="person-role">Managing Director</p>

    <p class="office"><strong>Office Address:</strong><br>
      Suite 307, Level 3, 82 Penhallow St<br>
      Sydney, NSW 2000, Australia</p>

    <div class="divider"></div>

    <dl class="contact contact--email"><dt>Email:</dt><dd>dorianwhitcombe@velantra.com.au</dd></dl>
    <dl class="contact contact--phone"><dt>Phone:</dt><dd>+61 2 7315 2946</dd></dl>
    <dl class="contact contact--mobile"><dt>Mobile Phone:</dt><dd>+61 422 517 639</dd></dl>
  </section>
</body>
</html>
```